Create a Professional PowerPoint Slide Deck

I need a professional looking and editable PowerPoint presentation with contents based on the attached PDF.

I would like to see the following;
- add design elements to every slide (cover, title, contents etc)
- enhance the graphs or charts
- same copy will be used
I'm attaching the document to be put into powerpoint (KWRO white paper: "Cargo Wise")

Target Market(s)

Executives and managers responsible for the distribution of products

Industry/Entity Type

It Professional

Font styles to use
Serif

Colors

Designer to choose colors to be used in the design.

Requirements
Must have
• The format should be portrait orientation as this may be printed on paper and converted to PDF for distribution
• Complete conversion of all pages in the attached White Paper
• Upgraded graphics and formatting
Nice to have
• Any creative ideas to make the presentation more attractive or easier to understand
• Color scheme should complement the KWRO Freightlines Logo (red and black)

```html
<!DOCTYPE html>
<html lang="en">
<head>
<meta charset="utf-8">
<title>KWRO Freightlines White Paper – Use Your Data</title>
<link href="https://fonts.googleapis.com/css2?family=Roboto+Condensed:wght@400;700&family=Roboto:wght@300;400;700;900&display=swap" rel="stylesheet">
<style>
:root{
  --red:#e8231a;
  --black:#111111;
  --ink:#2a2a2a;
  --grey-text:#555;
  --panel:#efefef;
  --canvas:#cfcfcf;
  --steel:#3b8fd0;
  --navy:#2d4f80;
  --white:#ffffff;
}
*{box-sizing:border-box;margin:0;padding:0}
html,body{width:1200px;height:1143px;overflow:hidden;background:var(--canvas)}
body{position:relative;font-family:"Roboto",sans-serif;color:var(--ink)}
.page{position:absolute;width:384px;height:553px;background:var(--white);overflow:hidden;box-shadow:0 1px 3px rgba(0,0,0,.25)}
.p1{left:13px;top:12px}.p2{left:409px;top:12px}.p3{left:804px;top:12px}
.p4{left:13px;top:578px}.p5{left:409px;top:578px}.p6{left:804px;top:578px}
.tab{position:absolute;left:0;top:0;width:14px;height:64px;background:var(--red)}
.brand{position:absolute;left:24px;top:24px;display:flex;align-items:center;gap:5px}
.brand-dot{width:18px;height:18px;border-radius:50%;border:2px solid var(--black)}
.brand-name{font-family:"Roboto Condensed",sans-serif;font-weight:700;font-size:20px;letter-spacing:3px;color:var(--red)}
.running-title{position:absolute;right:29px;top:24px;text-align:right;font-size:9.6px;line-height:10.6px;letter-spacing:1.8px;color:var(--black)}
.running-title b{color:var(--red);font-weight:700}
.rule{position:absolute;left:0;height:1.6px;background:var(--black)}
.rule.a{top:84px;width:294px}
.rule.b{top:91px;left:294px;width:0}
.footer{position:absolute;left:0;bottom:0;width:100%;height:22px;background:var(--black);color:var(--white);font-size:8px;font-weight:700;text-align:center;line-height:22px}
.footer span{color:var(--red);font-weight:400}
.pageno{position:absolute;right:26px;bottom:0;width:26px;height:28px;background:var(--red);color:var(--white);font-size:11px;text-align:center;line-height:28px}
.banner{position:absolute;left:0;background:var(--red);color:var(--white);font-family:"Roboto Condensed",sans-serif;text-align:center}
.band{position:absolute;left:0;width:100%;background:var(--black)}
.copy{position:absolute;font-size:7.3px;line-height:10.2px;color:#444;text-align:justify;font-weight:300;overflow:hidden}
.grey-panel{position:absolute;left:0;width:100%;background:var(--panel)}
.subhead{position:absolute;font-family:"Roboto Condensed",sans-serif;color:var(--red);font-size:11px;line-height:13px}

/* cover */
.cover-label{position:absolute;right:20px;top:36px;font-family:"Roboto Condensed",sans-serif;font-size:13px;color:var(--black);font-weight:700}
.cover-label span{color:var(--red)}
.cover-title{position:absolute;left:31px;top:104px;font-family:"Roboto Condensed",sans-serif;font-size:24px;line-height:27px;color:var(--black)}
.cover-title b{color:var(--red)}
.cover-visual{position:absolute;left:0;top:210px;width:384px;height:168px}
.contact-col{position:absolute;left:40px;top:229px;width:36px;text-align:center;color:var(--white);font-size:4px}
.contact-col .ico{width:19px;height:19px;border-radius:50%;background:var(--white);margin:0 auto 4px;display:flex;align-items:center;justify-content:center}
.contact-col p{margin-bottom:17px;white-space:nowrap}
.cover-intro{position:absolute;left:31px;top:440px;width:200px;font-size:9px;line-height:12px;color:#444;font-weight:300;text-align:justify}
.cover-year{position:absolute;left:232px;top:424px;font-family:"Roboto",sans-serif;font-weight:900;font-size:56px;letter-spacing:-1px;color:var(--black)}
.cover-year span{color:var(--red)}

/* page 5 */
.section-title{position:absolute;left:32px;top:116px;font-family:"Roboto Condensed",sans-serif;font-weight:700;font-size:22px;line-height:26px;color:var(--black)}
.section-title span{color:var(--red)}
.fig-caption{position:absolute;font-size:7.2px;color:#444}

/* page 6 */
.touch-title{position:absolute;left:46px;top:106px;font-family:"Roboto Condensed",sans-serif;font-weight:700;font-size:24px;color:var(--black)}
.touch-lede{position:absolute;left:44px;top:146px;font-size:10px;line-height:13px;color:#777;font-weight:300}
.touch-item{position:absolute;left:44px;font-size:8.5px;color:#333}
.touch-icon{position:absolute;left:44px}
.social{position:absolute;left:0;top:350px;width:100%;height:60px;background:var(--black)}
.social i{position:absolute;top:12px;width:36px;height:36px;border-radius:50%;border:1.5px solid #777;background:#1c1c1c}
.skyline{position:absolute;left:0;top:410px;width:100%;height:143px;background:linear-gradient(160deg,#5a5a5a 0%,#d9d9d9 35%,#8a8a8a 60%,#2b2b2b 100%)}
</style>
</head>
<body>

<!-- Cover -->
<section class="page p1">
  <div class="tab"></div>
  <div class="brand"><i class="brand-dot"></i><span class="brand-name">KWRO</span></div>
  <div class="cover-label">KWRO Freightlines <span>White Paper</span></div>
  <div class="rule a"></div>
  <h1 class="cover-title"><b>Use Your Data</b> To Improve<br>Logistics Processes And Profits</h1>
  <svg class="cover-visual" viewBox="0 0 384 168" aria-hidden="false">
    <defs>
      <linearGradient id="darkFade" x1="0" x2="1"><stop offset="0" stop-color="#262d38"/><stop offset="1" stop-color="#4b5664"/></linearGradient>
      <linearGradient id="glass" x1="0" y1="0" x2="1" y2="1"><stop offset="0" stop-color="#8aa3b5"/><stop offset=".5" stop-color="#3f5a70"/><stop offset="1" stop-color="#6f8899"/></linearGradient>
      <linearGradient id="chev" x1="0" x2="1"><stop offset="0" stop-color="#ff2a1a"/><stop offset="1" stop-color="#8e0d08"/></linearGradient>
    </defs>
    <rect width="384" height="168" fill="url(#darkFade)"/>
    <rect x="176" y="10" width="208" height="158" fill="url(#glass)" role="img" aria-label="Photo of a glass office building facade"/>
    <polygon points="248,-40 264,-40 160,60 253,190 235,190 140,60" fill="url(#chev)"/>
    <polygon points="232,-40 240,-40 150,52 146,48" fill="#ffffff" opacity=".8"/>
  </svg>
  <div class="contact-col">
    <div class="ico"><svg width="9" height="9" viewBox="0 0 24 24"><path d="M6.6 10.8a15 15 0 006.6 6.6l2.2-2.2a1 1 0 011-.25 11 11 0 003.6.6 1 1 0 011 1V20a1 1 0 01-1 1A17 17 0 013 4a1 1 0 011-1h3.5a1 1 0 011 1 11 11 0 00.6 3.6 1 1 0 01-.25 1z" fill="#2a2a2a"/></svg></div>
    <p>+10 555 0148</p>
    <div class="ico"><svg width="9" height="9" viewBox="0 0 24 24"><path d="M3 5h18v14H3z" fill="#2a2a2a"/><path d="M3 5l9 7 9-7" stroke="#fff" stroke-width="2" fill="none"/></svg></div>
    <p>support@kwro.example</p>
    <div class="ico"><svg width="9" height="9" viewBox="0 0 24 24"><path d="M12 3l9 8h-3v9h-4v-6h-4v6H6v-9H3z" fill="#2a2a2a"/></svg></div>
    <p>88 Quay Rd</p>
  </div>
  <p class="cover-intro">You generate valuable information every time you ship. Don't let this data sit in the cloud, use it to improve your processes and reduce shipping costs. Identify trends before they become problems.</p>
  <div class="cover-year">20<span>18</span></div>
  <div class="footer" style="height:22px"></div>
</section>

<!-- Page 2 -->
<section class="page p2">
  <div class="tab"></div>
  <div class="brand"><i class="brand-dot"></i><span class="brand-name">KWRO</span></div>
  <div class="running-title"><b>Use Your Data</b> To Improve<br>Logistics Processes And<br>Profits</div>
  <div class="rule a"></div>
  <div class="band" style="top:110px;height:93px"></div>
  <div class="banner" style="top:104px;width:295px;height:20px;font-size:15px;line-height:20px">Profit from Shipping Smart</div>
  <p class="copy" style="left:20px;top:148px;width:344px;color:#ddd;font-size:6.8px;line-height:8.6px">The most meaningful way to differentiate your company from your competitors, the best way to put distance between you and the crowd is to do an outstanding job with information. How you gather, manage and use information will determine whether you win or lose.<br><b style="font-weight:700;font-size:5.6px">- Dana Whitfield</b></p>
  <p class="copy" style="left:26px;top:216px;width:160px;height:250px">When you ship freight, how do you ensure you are getting the best value? Value entails a combination of price, service, transit time and reputation of the carrier. It also entails the amount of time you and your staff spend obtaining quotes and setting up shipments. All of these things impact the total cost of shipping. Most shippers intuitively believe that it is a good idea to get several quotes, especially if you ship to many locations with no real concentration on specific lanes. Individual carriers may offer significantly different rates on the same lane based on their own load balancing needs. If a carrier has a lot of business going to a specific destination, they will not likely be offering robust discounts on that lane. However, if they have limited loads, you have a good chance of negotiating a lower price than with a carrier that has a lot of business on that lane. The idea of checking with more than one carrier makes sense and may result in savings.</p>
  <p class="copy" style="left:198px;top:216px;width:160px;height:176px">How to go about getting those multiple quotes, comparing them and deciding which carrier to choose? One way is to call or send emails to multiple carriers asking each of them for a quote (Fig. 1). When you get the responses, you choose the lowest price and tell them to come pick up your freight. This spot pricing method takes a bit of time and coordination, especially when you are handling multiple shipments each day. It also means that you will need to have an account and some sort of negotiated pricing with each of the carriers you are asking to quote. Other limitations to this method include multiple invoices and a lack of meaningful relationships with your carriers.</p>
  <svg style="position:absolute;left:191px;top:398px" width="168" height="122" viewBox="0 0 168 122">
    <defs><marker id="ah1" markerWidth="4" markerHeight="4" refX="3" refY="2" orient="auto"><path d="M0,0L4,2L0,4z" fill="#3b8fd0"/></marker></defs>
    <rect x=".5" y=".5" width="167" height="121" fill="#dfe3ef" stroke="#9aa"/>
    <rect x="131" y="1" width="29" height="120" fill="#8a8a8a"/>
    <text x="133" y="30" font-size="3.4" fill="#fff" font-family="Roboto,sans-serif"><tspan x="133">Figure 1.</tspan><tspan x="133" dy="4">Sending</tspan><tspan x="133" dy="4">multiple</tspan><tspan x="133" dy="4">quote</tspan><tspan x="133" dy="4">requests</tspan><tspan x="133" dy="4">to carriers,</tspan><tspan x="133" dy="4">evaluating</tspan><tspan x="133" dy="4">and then</tspan><tspan x="133" dy="4">awarding</tspan><tspan x="133" dy="4">the</tspan><tspan x="133" dy="4">business</tspan><tspan x="133" dy="4">takes up</tspan><tspan x="133" dy="4">valuable</tspan><tspan x="133" dy="4">time.</tspan></text>
    <text x="62" y="10" font-size="5.6" fill="#222" font-family="Roboto,sans-serif">Queries/Quotes</text>
    <text x="24" y="36" font-size="5.6" fill="#222" font-family="Roboto,sans-serif"><tspan x="24">Quotes/</tspan><tspan x="24" dy="6">Booking</tspan></text>
    <rect x="24" y="50" width="30" height="28" fill="#3b8fd0" stroke="#1c5d94"/>
    <text x="39" y="66" font-size="5.8" fill="#ffd21a" font-style="italic" font-weight="700" text-anchor="middle" font-family="Roboto,sans-serif">Shipper</text>
    <g stroke="#3b8fd0" stroke-width=".8" marker-end="url(#ah1)">
      <line x1="54" y1="64" x2="102" y2="16"/><line x1="54" y1="64" x2="102" y2="28"/><line x1="54" y1="64" x2="102" y2="40"/><line x1="54" y1="64" x2="102" y2="52"/><line x1="54" y1="64" x2="102" y2="64"/><line x1="54" y1="64" x2="102" y2="76"/><line x1="54" y1="64" x2="102" y2="88"/><line x1="54" y1="64" x2="102" y2="100"/><line x1="54" y1="64" x2="102" y2="112"/>
    </g>
    <g font-size="5" font-weight="700" fill="#fff" text-anchor="middle" font-family="Roboto,sans-serif">
      <circle cx="107" cy="16" r="4.5" fill="#2e7fc0"/><text x="107" y="18">T</text>
      <circle cx="107" cy="28" r="4.5" fill="#5cbf3a"/><text x="107" y="30">T</text>
      <circle cx="107" cy="40" r="4.5" fill="#2e7fc0"/><text x="107" y="42">T</text>
      <circle cx="107" cy="52" r="4.5" fill="#2e7fc0"/><text x="107" y="54">T</text>
      <circle cx="107" cy="64" r="4.5" fill="#2e7fc0"/><text x="107" y="66">T</text>
      <circle cx="107" cy="76" r="4.5" fill="#2e7fc0"/><text x="107" y="78">T</text>
      <circle cx="107" cy="88" r="4.5" fill="#2e7fc0"/><text x="107" y="90">T</text>
      <circle cx="107" cy="100" r="4.5" fill="#2e7fc0"/><text x="107" y="102">T</text>
      <circle cx="107" cy="112" r="4.5" fill="#2e7fc0"/><text x="107" y="114">T</text>
    </g>
  </svg>
  <div class="footer">KWRO Freightlines <span>White Paper</span></div>
  <div class="pageno">2</div>
</section>

<!-- Page 3 -->
<section class="page p3">
  <div class="tab"></div>
  <div class="brand"><i class="brand-dot"></i><span class="brand-name">KWRO</span></div>
  <div class="running-title"><b>Use Your Data</b> To Improve<br>Logistics Processes And<br>Profits</div>
  <div class="rule a"></div>
  <div class="band" style="top:114px;height:36px"></div>
  <div class="banner" style="top:96px;width:308px;height:44px;font-size:13.5px;line-height:15px;padding-top:7px">A Better Way to Handle Multiple Quotes – use a TMS<br>(Transportation Management System)</div>
  <div class="grey-panel" style="top:150px;height:170px"></div>
  <p class="copy" style="left:31px;top:160px;width:158px;height:156px">Is there a way to get multiple quotes without spending so much time and effort asking for quotes, reviewing them and then awarding the business? In a word, yes. If you use a Transportation Management System (TMS) you can enter the shipment information on your shipment once and get immediate quotes from multiple carriers (Fig. 2). You can select the carrier you want and get your shipment underway in about a minute. In addition to saving time and reducing stress, the TMS will permit you to print the BOL and Labels so your</p>
  <p class="copy" style="left:199px;top:160px;width:158px;height:156px">shipment is ready for the driver to pick up. You access the TMS via the web, so there is no special equipment to purchase. You will need accounts with each carrier and you should negotiate your own rates with them. The TMS will typically permit you to track shipments on all carriers, and it can also capture the quote information for reference later. Perhaps the most commonly overlooked, the data from all of your shipments is captured and retained in the TMS, so you can produce reports at the end of the month or on demand.</p>
  <div style="position:absolute;left:27px;top:324px;width:55px;height:176px;background:#555;color:#ddd;font-size:5.4px;line-height:6.8px;font-style:italic;padding:40px 5px 0 5px"><b>Figure 2.</b> Using a TMS saves time by entering the quote request, receiving multiple quotes, assigning the load and printing BOL and Shipping Labels in less than a minute</div>
  <div class="grey-panel" style="top:502px;height:30px"></div>
  <svg style="position:absolute;left:90px;top:324px" width="294" height="176" viewBox="0 0 294 176">
    <defs>
      <marker id="ah2" markerWidth="5" markerHeight="5" refX="4" refY="2.5" orient="auto"><path d="M0,0L5,2.5L0,5z" fill="#3b8fd0"/></marker>
      <marker id="ah2s" markerWidth="5" markerHeight="5" refX="1" refY="2.5" orient="auto"><path d="M5,0L0,2.5L5,5z" fill="#3b8fd0"/></marker>
    </defs>
    <text x="174" y="20" font-size="8.5" fill="#222" font-family="Roboto,sans-serif">Queries/Quotes</text>
    <text x="103" y="53" font-size="8" fill="#222" text-anchor="middle" font-family="Roboto,sans-serif"><tspan x="103">Quotes/</tspan><tspan x="103" dy="9">Booking</tspan></text>
    <text x="103" y="120" font-size="8" fill="#222" text-anchor="middle" font-family="Roboto,sans-serif"><tspan x="103">Historical</tspan><tspan x="103" dy="9">Data</tspan></text>
    <rect x="36" y="72" width="48" height="38" fill="#3b8fd0" stroke="#1c5d94"/>
    <text x="60" y="94" font-size="8.5" fill="#ffd21a" font-style="italic" font-weight="700" text-anchor="middle" font-family="Roboto,sans-serif">Shipper</text>
    <line x1="86" y1="91" x2="120" y2="91" stroke="#3b8fd0" stroke-width="1.4" marker-end="url(#ah2)" marker-start="url(#ah2s)"/>
    <rect x="122" y="75" width="36" height="32" rx="3" fill="#3b8fd0" stroke="#1c5d94"/>
    <text x="140" y="94" font-size="8.5" fill="#fff" font-style="italic" font-weight="700" text-anchor="middle" font-family="Roboto,sans-serif">TMS</text>
    <g stroke="#3b8fd0" stroke-width="1.1" marker-end="url(#ah2)">
      <line x1="158" y1="91" x2="211" y2="28"/><line x1="158" y1="91" x2="211" y2="44"/><line x1="158" y1="91" x2="211" y2="60"/><line x1="158" y1="91" x2="211" y2="76"/><line x1="158" y1="91" x2="211" y2="92"/><line x1="158" y1="91" x2="211" y2="108"/><line x1="158" y1="91" x2="211" y2="124"/><line x1="158" y1="91" x2="211" y2="140"/><line x1="158" y1="91" x2="211" y2="156"/>
    </g>
    <g font-size="6.5" font-weight="700" fill="#fff" text-anchor="middle" font-family="Roboto,sans-serif">
      <circle cx="218" cy="28" r="6" fill="#2e7fc0"/><text x="218" y="30.5">T</text>
      <circle cx="218" cy="44" r="6" fill="#5cbf3a"/><text x="218" y="46.5">T</text>
      <circle cx="218" cy="60" r="6" fill="#2e7fc0"/><text x="218" y="62.5">T</text>
      <circle cx="218" cy="76" r="6" fill="#2e7fc0"/><text x="218" y="78.5">T</text>
      <circle cx="218" cy="92" r="6" fill="#2e7fc0"/><text x="218" y="94.5">T</text>
      <circle cx="218" cy="108" r="6" fill="#2e7fc0"/><text x="218" y="110.5">T</text>
      <circle cx="218" cy="124" r="6" fill="#2e7fc0"/><text x="218" y="126.5">T</text>
      <circle cx="218" cy="140" r="6" fill="#2e7fc0"/><text x="218" y="142.5">T</text>
      <circle cx="218" cy="156" r="6" fill="#2e7fc0"/><text x="218" y="158.5">T</text>
    </g>
  </svg>
  <div class="footer">KWRO Freightlines <span>White Paper</span></div>
  <div class="pageno">3</div>
</section>

<!-- Page 4 -->
<section class="page p4">
  <div class="tab"></div>
  <div class="brand"><i class="brand-dot"></i><span class="brand-name">KWRO</span></div>
  <div class="running-title"><b>Use Your Data</b> To Improve<br>Logistics Processes And<br>Profits</div>
  <div class="rule a" style="width:192px"></div>
  <div class="band" style="top:112px;height:26px"></div>
  <div class="banner" style="top:102px;width:296px;height:25px;font-size:15px;line-height:25px">Beyond the TMS – Using a 3PL</div>
  <div class="grey-panel" style="top:138px;height:124px"></div>
  <p class="copy" style="left:31px;top:146px;width:322px;height:112px">TMS systems are commonly web based and very easy to use. They usually require a monthly fee depending on the number of users and monthly shipments. There may also be a fee for setting up your carriers in the system to get started. What else can you do to improve your logistics system? If you utilize the services of a 3PL, you will often be able to get a TMS system for no charge as long as you book with their carriers. The 3PL is bringing much more business to the negotiating table than you will alone, so their rates are likely to be lower than yours. So, you get lower rates, spend less time quoting and booking as well as all the other benefits of a TMS while saving money. You also get a single invoice each month covering all of your shipments.</p>
  <h3 class="subhead" style="left:31px;top:286px;width:152px">3PL's Help You Select the Best Mode at the Best Price</h3>
  <h3 class="subhead" style="left:203px;top:286px;width:152px">Data Stuck In the Cloud Is No Earthly Good</h3>
  <p class="copy" style="left:31px;top:326px;width:150px;height:160px">With a 3PL, you also have access to a knowledgeable staff who can help you when your loads might be better served with a partial truckload or full truckload quote. Some 3PL's provide for putting your carriers in the TMS alongside their carriers and all the carriers bid against each other. If your carrier is selected, you will receive a bill from them and deal directly with them for any service issues. If you use the 3PL's carriers, you get a combined invoice from the 3PL.</p>
  <p class="copy" style="left:203px;top:326px;width:150px;height:172px">Your logistics system is constantly generating data including pricing by lane, cost per pound, "geographic center of gravity," and much more. To ignore this information is to lose a great opportunity to understand your system at a deeper level and make informed decisions to improve your performance. Whether it is a big deal like establishing a new distribution center that will result in shorter delivery times at less cost or relatively simple things like combining loads to take advantage of weight breaks, you will benefit greatly from mining the information your system contains.</p>
  <div class="footer">KWRO Freightlines <span>White Paper</span></div>
  <div class="pageno">4</div>
</section>

<!-- Page 5 -->
<section class="page p5">
  <div class="tab"></div>
  <div class="brand"><i class="brand-dot"></i><span class="brand-name">KWRO</span></div>
  <div class="running-title"><b>Use Your Data</b> To Improve<br>Logistics Processes And<br>Profits</div>
  <div class="rule a" style="width:192px"></div>
  <div class="rule" style="top:82px;left:192px;width:100px;height:1px"></div>
  <h2 class="section-title">Data Must be <span>Processed and<br>Evaluated</span> Properly to Be Useful</h2>
  <p class="copy" style="left:32px;top:198px;width:320px;height:76px;font-size:7.6px">KWRO can help organize, analyze and utilize your data. KWRO arranges for our clients to work with major 3PL's providing access not only to their robust TMS systems, but also their volume based pricing. You get all the benefits of a TMS, plus better rates. You also get custom analysis of your data prepared by KWRO from the information captured and stored in the TMS. When your information is exported from the TMS, it comes out in a spreadsheet with no formatting, filtering or meaningful summaries (Fig 3).</p>
  <svg style="position:absolute;left:55px;top:288px" width="256" height="218" viewBox="0 0 256 218">
    <defs>
      <pattern id="rows" width="256" height="6.4" patternUnits="userSpaceOnUse">
        <rect x="6" y="2" width="26" height="2" fill="#999"/><rect x="36" y="2" width="14" height="2" fill="#999"/><rect x="54" y="2" width="28" height="2" fill="#999"/><rect x="100" y="2" width="10" height="2" fill="#999"/><rect x="140" y="2" width="10" height="2" fill="#aaa"/><rect x="174" y="2" width="20" height="2" fill="#999"/><rect x="212" y="2" width="8" height="2" fill="#999"/>
        <line x1="0" y1="6.3" x2="256" y2="6.3" stroke="#e4e4e4" stroke-width=".4"/>
      </pattern>
    </defs>
    <rect width="256" height="218" fill="#fff" stroke="#ddd"/>
    <g font-size="3.4" fill="#333" font-family="Roboto,sans-serif">
      <text x="6" y="6">Client</text><text x="36" y="6">Waybill</text><text x="54" y="6">Ship Date</text><text x="72" y="6">Status</text><text x="100" y="6">Receiver</text><text x="140" y="6">Receiver Zip</text><text x="174" y="6">Lane</text><text x="206" y="6">Freight Total</text>
    </g>
    <rect x="0" y="8" width="256" height="208" fill="url(#rows)"/>
  </svg>
  <p class="fig-caption" style="left:0;width:384px;text-align:center;top:512px"><b>Figure 3.</b> Lots of data, not much help</p>
  <div class="footer">KWRO Freightlines <span>White Paper</span></div>
  <div class="pageno">5</div>
</section>

<!-- Page 6 -->
<section class="page p6">
  <div class="tab"></div>
  <div class="brand"><i class="brand-dot"></i><span class="brand-name">KWRO</span></div>
  <div class="running-title"><b>Use Your Data</b> To Improve<br>Logistics Processes And<br>Profits</div>
  <div class="rule a" style="width:192px"></div>
  <div class="rule" style="top:82px;left:192px;width:100px;height:1px"></div>
  <h2 class="touch-title">Get In Touch</h2>
  <p class="touch-lede">Morsum desna consd treuda mero them<br>berga es in the consda co nurtda.</p>
  <svg class="touch-icon" style="top:182px" width="22" height="22" viewBox="0 0 24 24"><circle cx="12" cy="12" r="10" fill="none" stroke="#111" stroke-width="1.8"/><path d="M8.5 7.5c.5-.5 1.2-.5 1.5 0l1 2c.2.4 0 .8-.3 1.1l-.6.5a6 6 0 003 3l.5-.6c.3-.3.7-.5 1.1-.3l2 1c.5.3.5 1 0 1.5-1 1-2.6 1.2-4 .4a11 11 0 01-4.6-4.6c-.8-1.4-.6-3 .4-4z" fill="#111"/></svg>
  <p class="touch-item" style="top:211px">00 -5550 19 284 730</p>
  <svg class="touch-icon" style="top:238px" width="24" height="16" viewBox="0 0 24 16"><rect x="1" y="1" width="22" height="14" fill="none" stroke="#111" stroke-width="1.6"/><path d="M1 1l11 8 11-8" fill="none" stroke="#111" stroke-width="1.6"/></svg>
  <p class="touch-item" style="top:259px">hello@kwro.example</p>
  <svg class="touch-icon" style="top:274px" width="18" height="22" viewBox="0 0 18 22"><path d="M9 1a7 7 0 017 7c0 5-7 13-7 13S2 13 2 8a7 7 0 017-7z" fill="none" stroke="#111" stroke-width="1.6"/><circle cx="9" cy="8" r="2.5" fill="none" stroke="#111" stroke-width="1.6"/></svg>
  <p class="touch-item" style="top:306px">77 Harbor Lane, Dock Street 210</p>
  <div class="social" aria-label="Social channels">
    <i style="left:46px"></i><i style="left:110px"></i><i style="left:174px"></i><i style="left:238px"></i><i style="left:301px"></i>
  </div>
  <div class="skyline" role="img" aria-label="Black and white photo looking up at glass skyscrapers"></div>
</section>

</body>
</html>
```